Health Bar Packaging

Need packaging for a range of new health bars.
4 different types, 24 flavours (just submit a single bar or two)
I want all the bars to look basically the same (different types can have a text colour change or strip and flavours can have different images).

Need a striking design to compete against other similar bars on the shelves of health food stores.

Our biggest competitor would be www.larkmorefoods.com who has similar bars (ingredients)

I have included a design that I made to show an example (Jpg attached). You can either submit new designs or use the same concept and alter what you think will work to make the range stand out from the other similar bars on health food shop shelves. Required information text is also shown such as ‘sugar free’ etc.

I also need a design for the display/packaging boxes (Example in Pdf attached)

A template is attached for reference and to be used for the successful designs final print ready design only (shows size). The easy peel strip should be able to be moved left or right but not up or down.
I have also attached a Pdf with the flavours listed and sample images for reference only, plus a Pdf with other bar designs already on the market.

Printing is going to be on silver foil so that can be used as part pf the design effect.

In case it makes a difference -
Printing is to be done via Gravure (rotogravure) method.
Each cylinder has the ability to print 8 designs in the same colour (width allows for 8 templates).
Each cylinder obviously incurs an additional cost so colours should be limited where possible but only if it doesn't affect quality.
I think its usually 5-8 colours max for this type of print.

Designer will be provided with further work for promotional items including floor displays, posters, flyers and shirts etc.

My logo is also attached but it isn't important to make it stand out so long as the bars can be identified with a name.

All the best.

Target Market(s)

Health Conscious, Weight Loss, Muscle Gain, Diabetics, Gluten Intolerant, Fitness

Industry/Entity Type

Graphic Design

Requirements
Must have
• Clean, standout design.
• The words -
• 'Raw Protein Bar'
• 'Sugar Free'
• 'Gluten Free'
• 'Soy Free'
• 'High Protein'
• 'High Fiber'
• 'No Fruit'
• 'No Sugar Alcohols'
• 'Low Carb'
• Natural Range -
• 'All natural ingredients, no artificial sweeteners, colours or flavours'
• White Chocolate Range -
• 'With added sugar free white chocolate chips'
• Chocolate Range -
• 'With added sugar free chocolate chips'
Nice to have
• A minor change between the ranges such as a text colour change or area.
• So the bars look uniform

```html
<!DOCTYPE html>
<html lang="en">
<head>
<meta charset="utf-8">
<title>Keenfield Protein Bar – Wrapper Range</title>
<link href="https://fonts.googleapis.com/css2?family=Fjalla+One&family=Fresca&family=Merienda:wght@700&family=Economica:wght@400;700&display=swap" rel="stylesheet">
<style>
  :root{
    --bg:#5e3920;
    --foil:#ffffff;
    --pleat:#d9d9d9;
    --gold:#d6b46a;
    --gold-deep:#b8903f;
    --purple:#4a2e7c;
    --cream:#f7e9c9;
    --amber:#f2b73f;
    --red:#d0322c;
    --brown-text:#4a2b1a;
    --star:#c8231f;
  }
  *{box-sizing:border-box;margin:0;padding:0}
  html,body{width:1200px;height:1027px;overflow:hidden}
  body{background:var(--bg);position:relative;font-family:"Economica",sans-serif}
  .wrapper{position:absolute;width:780px;height:342px}
  .wrapper--cookies{left:186px;top:127px}
  .wrapper--white{left:192px;top:573px}
  .wrapper__shape{position:absolute;inset:0;width:780px;height:342px}
  .wrapper__photo{position:absolute}
  .wrapper--cookies .wrapper__photo{left:438px;top:50px;width:294px;height:222px;border-radius:40px;
    background:radial-gradient(ellipse at 55% 50%,#4a3a36 0%,#2f2220 60%,rgba(47,34,32,0) 75%)}
  .wrapper--white .wrapper__photo{left:430px;top:20px;width:344px;height:290px;
    background:linear-gradient(160deg,#fbf3e3 0%,#f1e2c6 55%,#e6d2ae 100%);
    clip-path:polygon(18% 8%,100% 0,100% 80%,20% 100%,2% 55%)}
  .title{position:absolute;left:77px;top:62px;font-family:"Fjalla One",sans-serif;font-size:47px;letter-spacing:.5px;line-height:1}
  .wrapper--cookies .title{color:var(--cream)}
  .wrapper--white .title{color:var(--red);text-shadow:0 0 2px #fff,1px 1px 0 #fff,-1px -1px 0 #fff}
  .flavour-label{position:absolute;left:95px;top:114px;font-family:"Merienda",cursive;font-size:17px;color:var(--gold)}
  .wrapper--white .flavour-label{color:var(--red)}
  .flavour-name{position:absolute;left:113px;top:126px;font-family:"Fresca",sans-serif;font-size:38px;line-height:1}
  .wrapper--cookies .flavour-name{color:var(--cream)}
  .wrapper--white .flavour-name{color:var(--cream);-webkit-text-stroke:1.2px var(--red);paint-order:stroke fill}
  .claims{position:absolute;left:92px;top:230px;display:grid;grid-template-columns:repeat(3,auto);column-gap:14px;row-gap:6px;
    font-size:22px;color:var(--brown-text)}
  .claims span{display:flex;align-items:center;gap:14px}
  .claims .star{color:var(--star);font-size:16px}
  .net-wt{position:absolute;left:586px;top:286px;font-family:"Fjalla One",sans-serif;font-size:12px;color:var(--brown-text)}
  .badge{position:absolute;width:96px;height:96px;border-radius:50%;background:#fff;
    box-shadow:0 2px 4px rgba(0,0,0,.25);display:flex;align-items:center;justify-content:center}
  .wrapper--cookies .badge{left:404px;top:146px}
  .wrapper--white .badge{left:404px;top:146px}
  .badge__seal{width:80px;height:80px;border-radius:50%;
    background:radial-gradient(circle at 40% 35%,#f3dc9c,var(--gold) 55%,var(--gold-deep));
    display:flex;align-items:center;justify-content:center;text-align:center;
    font-family:"Fjalla One",sans-serif;font-size:8.5px;line-height:1.25;color:#3d2a14}
  .maker{position:absolute;left:636px;top:40px;display:flex;align-items:center;gap:5px}
  .maker__mark{width:14px;height:14px;background:var(--red)}
  .maker__name{font-family:"Fjalla One",sans-serif;font-size:11px;color:var(--cream)}
</style>
</head>
<body>
<svg width="0" height="0" style="position:absolute">
  <defs>
    <pattern id="teeth-left" width="6" height="8" patternUnits="userSpaceOnUse">
      <polygon points="6,0 0,4 6,8" fill="#fff"/>
    </pattern>
    <pattern id="teeth-right" width="6" height="8" patternUnits="userSpaceOnUse">
      <polygon points="0,0 6,4 0,8" fill="#fff"/>
    </pattern>
    <pattern id="pleats" width="4" height="10" patternUnits="userSpaceOnUse">
      <rect width="1.2" height="10" fill="#000" opacity=".12"/>
    </pattern>
  </defs>
</svg>

<article class="wrapper wrapper--cookies">
  <svg class="wrapper__shape" viewBox="0 0 780 342" aria-hidden="true">
    <rect x="6" y="0" width="768" height="342" fill="var(--foil)"/>
    <rect x="0" y="0" width="6" height="342" fill="url(#teeth-left)"/>
    <rect x="774" y="0" width="6" height="342" fill="url(#teeth-right)"/>
    <path d="M0 0 H780 V160 Q520 172 320 186 Q130 198 0 200 Z" fill="var(--purple)"/>
    <path d="M0 208 Q130 206 320 194 Q520 180 780 168" fill="none" stroke="var(--gold)" stroke-width="5"/>
    <rect x="0" y="0" width="32" height="342" fill="url(#pleats)"/>
    <rect x="748" y="0" width="32" height="342" fill="url(#pleats)"/>
  </svg>
  <div class="wrapper__photo" role="img" aria-label="Stack of chocolate sandwich cookies with cream filling"></div>
  <div class="maker"><span class="maker__mark"></span><span class="maker__name">Keenfield</span></div>
  <h2 class="title">KEENFIELD PROTEIN BAR</h2>
  <p class="flavour-label">Flavour</p>
  <p class="flavour-name">cream and cookies</p>
  <div class="badge"><div class="badge__seal">PREBIOTIC RAW<br>PROTEIN BAR</div></div>
  <div class="claims">
    <span>Low Carb <b class="star">★</b></span><span>Low Fat <b class="star">★</b></span><span>high fibre</span>
    <span>Gluten Free <b class="star">★</b></span><span>Sugar Free <b class="star">★</b></span><span>Soy Free</span>
  </div>
  <p class="net-wt">NET WT. 2OZ (60G)</p>
</article>

<article class="wrapper wrapper--white">
  <svg class="wrapper__shape" viewBox="0 0 780 342" aria-hidden="true">
    <rect x="6" y="0" width="768" height="342" fill="var(--foil)"/>
    <rect x="0" y="0" width="6" height="342" fill="url(#teeth-left)"/>
    <rect x="774" y="0" width="6" height="342" fill="url(#teeth-right)"/>
    <path d="M0 0 H780 V160 Q520 172 320 186 Q130 198 0 200 Z" fill="var(--amber)"/>
    <path d="M0 208 Q130 206 320 194 Q520 180 780 168" fill="none" stroke="var(--gold)" stroke-width="5"/>
    <rect x="0" y="0" width="32" height="342" fill="url(#pleats)"/>
    <rect x="748" y="0" width="32" height="342" fill="url(#pleats)"/>
  </svg>
  <div class="wrapper__photo" role="img" aria-label="Broken squares of white chocolate bar"></div>
  <h2 class="title">KEENFIELD PROTEIN BAR</h2>
  <p class="flavour-label">Flavour</p>
  <p class="flavour-name">White Chocolate</p>
  <div class="badge"><div class="badge__seal">PREBIOTIC RAW<br>PROTEIN BAR</div></div>
  <div class="claims">
    <span>Low Carb <b class="star">★</b></span><span>Low Fat <b class="star">★</b></span><span>high fibre</span>
    <span>Gluten Free <b class="star">★</b></span><span>Sugar Free <b class="star">★</b></span><span>Soy Free</span>
  </div>
  <p class="net-wt">NET WT. 2OZ (60G)</p>
</article>
</body>
</html>
```